Business Stationary, Letterhead, Fax Cover Sheet, Client Intake, Email Signature, Thank you cards.
Marwick Law Firm
Business Stationary, Letterhead, Fax Cover Sheet, Client Intake, Email Signature, Thank you cards. - Law
Creative Brief
Professional
Len Marwick
Lawyer
2837 Falbrook St., Suite 1940 Houston, Texas 77014
len@marwick-law.example
www.marwick-law.example
Please note this project is Not for just One Person but for All Staff. The files should be in editable format to allow for different names and titles on cards.

```html
<!DOCTYPE html>
<html lang="en">
<head>
<meta charset="utf-8">
<title>Marwick Law Firm – Stationery Set</title>
<link rel="stylesheet" href="https://fonts.googleapis.com/css2?family=Cinzel:wght@700&family=Open+Sans:wght@400;600&display=swap">
<style>
:root{
  --bg:#eceff1;
  --paper:#ffffff;
  --ink:#3a3f45;
  --muted:#8a9096;
  --brand:#2a7fc1;
  --navy:#1a1f6e;
  --royal:#2b3fb8;
  --sky:#5fa7e8;
  --rule:#b9bec4;
  --faint:#e6ecf3;
  --black:#0c0c10;
  --flap:#1d1f2a;
}
*{margin:0;padding:0;box-sizing:border-box}
html,body{width:1200px;height:552px;overflow:hidden;background:var(--bg)}
body{position:relative;font-family:"Open Sans",Arial,sans-serif;color:var(--ink)}
.sheet,.card,.envelope{position:absolute;background:var(--paper);box-shadow:0 1px 4px rgba(0,0,0,.18);overflow:hidden}
.fax-sheet{left:34px;top:29px;width:352px;height:497px}
.letterhead{left:403px;top:29px;width:353px;height:497px}
.card-front{left:773px;top:29px;width:199px;height:115px}
.card-back{left:984px;top:29px;width:197px;height:115px;background:var(--black);border-radius:8px}
.envelope-front{left:773px;top:168px;width:408px;height:216px}
.envelope-back{left:773px;top:408px;width:408px;height:118px;background:var(--black)}

.wordmark{font-family:"Cinzel",Georgia,serif;font-weight:700;color:var(--brand);line-height:1.1;text-align:center;letter-spacing:.04em;white-space:nowrap}
.wordmark .dot{display:block;width:12px;height:12px;border-radius:50%;background:var(--brand);margin:0 auto 4px}
.sheet .wordmark{position:absolute;left:16px;top:14px;font-size:13px}
.contact{position:absolute;font-style:normal;font-size:5.5px;line-height:1.55;color:var(--muted)}
.sheet .contact{right:22px;top:16px;width:100px}
.watermark{position:absolute;left:0;right:0;top:205px;font-family:"Cinzel",Georgia,serif;font-weight:700;font-size:40px;color:var(--faint);text-align:center;letter-spacing:.06em}

.band{position:absolute;left:0;bottom:0;width:100%;background:linear-gradient(90deg,var(--navy),var(--royal) 60%,var(--sky))}
.sheet .band{height:34px}
.card .band{height:16px}
.envelope-front .band{height:26px}

.fax-title{position:absolute;right:22px;top:66px;font-size:8px;font-weight:600;letter-spacing:.1em}
.fax-table{position:absolute;left:14px;top:78px;width:324px;border-collapse:collapse;font-size:6px}
.fax-table td{border:1px solid var(--rule);height:17px;padding:0 4px}
.fax-table .label{width:38px}
.fax-options{position:absolute;left:14px;top:156px;display:flex;gap:18px;font-size:6px}
.fax-options span::before{content:"";display:inline-block;width:6px;height:6px;border:1px solid var(--ink);margin-right:3px;vertical-align:-1px}

.card-front .wordmark{position:absolute;left:12px;top:14px;font-size:8.5px}
.card-front .wordmark .dot{width:7px;height:7px}
.card-front .person{position:absolute;left:88px;top:10px;font-size:5.5px;line-height:1.45;color:var(--muted)}
.card-front .person strong{color:var(--ink);font-weight:600}
.card-back .wordmark{position:absolute;left:0;right:0;top:30px;font-size:11px}
.card-back .wordmark .dot{width:8px;height:8px}

.envelope-front .wordmark{position:absolute;left:18px;top:14px;font-size:11px}
.envelope-front .wordmark .dot{width:8px;height:8px}
.envelope-front .contact{left:88px;top:90px;width:110px}
.envelope-back .flap{position:absolute;left:0;top:0;width:100%;height:36px;background:var(--flap)}
.envelope-back .wordmark{position:absolute;left:0;right:0;top:56px;font-size:10px}
.envelope-back .wordmark .dot{width:8px;height:8px}
</style>
</head>
<body>

<section class="sheet fax-sheet" aria-label="Fax cover sheet">
  <div class="wordmark"><span class="dot"></span>MARWICK<br>LAW FIRM</div>
  <address class="contact">2837 Falbrook St., Suite 1940<br>Houston, Texas 77014<br>Tel (713) 555-0148<br>len@marwick-law.example<br>www.marwick-law.example</address>
  <div class="fax-title">FAX</div>
  <table class="fax-table">
    <tr><td class="label">To:</td><td></td><td class="label">From:</td><td></td></tr>
    <tr><td class="label">Fax:</td><td></td><td class="label">Pages:</td><td></td></tr>
    <tr><td class="label">Phone:</td><td></td><td class="label">Date:</td><td></td></tr>
    <tr><td class="label">Re:</td><td></td><td class="label">Cc:</td><td></td></tr>
  </table>
  <div class="fax-options"><span>Urgent</span><span>For Review</span><span>Please Comment</span><span>Please Reply</span><span>Please Recycle</span></div>
  <div class="watermark">MARWICK</div>
  <div class="band" role="img" aria-label="Decorative blue band along the bottom edge"></div>
</section>

<section class="sheet letterhead" aria-label="Letterhead">
  <div class="wordmark"><span class="dot"></span>MARWICK<br>LAW FIRM</div>
  <address class="contact">2837 Falbrook St., Suite 1940<br>Houston, Texas 77014<br>Tel (713) 555-0148<br>len@marwick-law.example<br>www.marwick-law.example</address>
  <div class="watermark">MARWICK</div>
  <div class="band" role="img" aria-label="Decorative blue band along the bottom edge"></div>
</section>

<section class="card card-front" aria-label="Business card front">
  <div class="wordmark"><span class="dot"></span>MARWICK<br>LAW FIRM</div>
  <div class="person"><strong>Len Marwick</strong><br>Lawyer<br><br>2837 Falbrook St., Suite 1940<br>Houston, Texas 77014<br>len@marwick-law.example<br>www.marwick-law.example</div>
  <div class="band" role="img" aria-label="Decorative blue band along the bottom edge"></div>
</section>

<section class="card card-back" aria-label="Business card back">
  <div class="wordmark"><span class="dot"></span>MARWICK<br>LAW FIRM</div>
  <div class="band" role="img" aria-label="Decorative blue band along the bottom edge"></div>
</section>

<section class="envelope envelope-front" aria-label="Envelope front">
  <div class="wordmark"><span class="dot"></span>MARWICK<br>LAW FIRM</div>
  <address class="contact">Len Marwick<br>2837 Falbrook St., Suite 1940<br>Houston, Texas 77014<br>www.marwick-law.example</address>
  <div class="band" role="img" aria-label="Decorative blue band along the bottom edge"></div>
</section>

<section class="envelope envelope-back" aria-label="Envelope back">
  <div class="flap"></div>
  <div class="wordmark"><span class="dot"></span>MARWICK<br>LAW FIRM</div>
</section>
</body>
</html>
```